Plakat-Design für Hypnose-Coaching
Zielgruppe
ich biete Hypnose-Sitzungen zur Auflösung des Glaubenssatzes 'Nicht gut genug?' Wir finden die Ursachen und lösen sie auf.
Meine Zielgruppe sind Frauen und teilweise auch Männer die sich im Berufsalltag aus Angst vor Zurückweisung oft unterordnen. Das, was sie sich fragen ist:
'Wieso schaffen es andere Menschen mit bestimmten Gesten oder Äußerungen, dass ich mich schlecht fühle?'
Aufgabenstellung
es soll ein DINA 4 Flyer werden.
'Nicht gut genug?'
Kindheitsmuster erkennen und auflösen
'Warum schaffen es andere Menschen mit Gesten oder Äußerungen, dass ich mich schlecht fühle?'
das war gestern! jetzt Termin vereinbaren: Hypnose-Coaching Henrik Dollmann Tel: 01563 8804257

```html
<!DOCTYPE html>
<html lang="de">
<head>
<meta charset="utf-8">
<title>Nicht gut genug? – Hypnose-Coaching Henrik Dollmann</title>
<link rel="stylesheet" href="https://fonts.googleapis.com/css2?family=Cabin:wght@400;500;600;700&display=swap">
<style>
  :root {
    --brand-blue: #1c54a0;
    --ink: #111111;
    --paper: #ffffff;
    --photo-grey-a: #d9d9d9;
    --photo-grey-b: #8d8d8d;
    --photo-warm-a: #c9a27a;
    --photo-warm-b: #4a4a52;
    --sign-blue-a: #9aa0a6;
    --sign-blue-b: #1f5597;
    --portrait-a: #b08a72;
    --portrait-b: #3b3f48;
    --badge-ring: #9fb3c2;
  }
  * { box-sizing: border-box; margin: 0; padding: 0; }
  html, body { width: 866px; height: 1200px; overflow: hidden; background: var(--paper); }
  .poster {
    position: relative;
    width: 866px;
    height: 1200px;
    background: var(--paper);
    font-family: "Cabin", "Helvetica Neue", Arial, sans-serif;
    color: var(--ink);
    overflow: hidden;
  }
  .hero-photos {
    position: absolute;
    left: 0; top: 6px;
    width: 866px; height: 324px;
    background: linear-gradient(90deg, var(--photo-grey-a) 0%, var(--photo-grey-b) 48%, var(--photo-warm-b) 52%, var(--photo-warm-a) 100%);
  }
  .hero-rule {
    position: absolute;
    left: 0; top: 342px;
    width: 866px; height: 6px;
    background: var(--brand-blue);
  }
  .headline {
    position: absolute;
    left: 32px; top: 388px;
    font-size: 106px;
    font-weight: 600;
    line-height: 1;
    color: var(--brand-blue);
    white-space: nowrap;
    letter-spacing: -1px;
  }
  .subline {
    position: absolute;
    left: 35px; top: 522px;
    font-size: 40px;
    font-weight: 700;
    line-height: 1.1;
    white-space: nowrap;
  }
  .question {
    position: absolute;
    left: 37px; top: 600px;
    width: 440px;
    font-size: 32px;
    font-weight: 400;
    line-height: 44.5px;
  }
  .claim {
    position: absolute;
    left: 35px; top: 818px;
    font-size: 58px;
    font-weight: 600;
    color: var(--brand-blue);
    white-space: nowrap;
    letter-spacing: -0.5px;
  }
  .signpost {
    position: absolute;
    left: 512px; top: 607px;
    width: 332px; height: 350px;
    background: linear-gradient(160deg, var(--sign-blue-a) 0%, var(--sign-blue-b) 60%, var(--sign-blue-a) 100%);
  }
  .portrait {
    position: absolute;
    left: 37px; top: 980px;
    width: 262px; height: 147px;
    background: linear-gradient(120deg, var(--portrait-b) 0%, var(--portrait-a) 45%, var(--portrait-b) 100%);
  }
  .footer-band {
    position: absolute;
    left: 37px; top: 1140px;
    right: 0; bottom: 0;
    background: var(--brand-blue);
  }
  .seal {
    position: absolute;
    left: 234px; top: 1052px;
    width: 124px; height: 124px;
  }
  .contact {
    position: absolute;
    left: 365px; top: 1002px;
    font-size: 27px;
    line-height: 31px;
    white-space: nowrap;
  }
  .contact-lead { font-weight: 700; }
</style>
</head>
<body>
<main class="poster">
  <div class="hero-photos" role="img" aria-label="Fotocollage im Puzzle-Look: links in Graustufen ein ausgegrenztes Mädchen und spottende Kinder, rechts in Farbe ein schreiender Vorgesetzter und eine niedergeschlagene Mitarbeiterin im Büro"></div>
  <div class="hero-rule"></div>

  <h1 class="headline">Nicht gut genug?</h1>
  <p class="subline">Kindheitsmuster erkennen und auflösen</p>

  <p class="question">Warum schaffen es andere Menschen mit Gesten oder Äußerungen, dass ich mich schlecht fühle?</p>

  <p class="claim">Das war gestern!</p>

  <div class="signpost" role="img" aria-label="Foto eines Wegweisers mit blauen Schildern „GESTERN“ nach links und „HEUTE“ nach rechts"></div>

  <div class="footer-band"></div>
  <div class="portrait" role="img" aria-label="Porträtfoto des Hypnose-Coaches Henrik Dollmann"></div>

  <svg class="seal" viewBox="0 0 124 124" aria-hidden="true">
    <circle cx="62" cy="62" r="62" fill="#ffffff"/>
    <circle cx="62" cy="62" r="54" fill="none" stroke="var(--badge-ring)" stroke-width="3"/>
    <circle cx="62" cy="62" r="34" fill="#1a7f8e"/>
  </svg>

  <div class="contact">
    <p class="contact-lead">Jetzt Termin vereinbaren:</p>
    <p>Hypnose-Coaching Henrik Dollmann</p>
    <p>Tel: 01563 8804257</p>
  </div>
</main>
</body>
</html>
```